TORLEX, Inc. new buisness cards - brand guide included

We need new business cards. SLEAK SIMPLE FINANCE. They must include a place for NAME, TITLE, CELL, OFFICE PHONE, EMAIL. they also must include our services across the bottom. AIR, OCEAN, FTL, LTL, EXPRESS. for reference this will be being handed to some of the most prestigious shipping companies in a america.

Target Market(s)

Finance and corporate

Contact Information for Business Card

We need new business cards. SLEAK SIMPLE FINANCE. They must include a place for NAME, TITLE, CELL, OFFICE PHONE, EMAIL. they also must include our services across the bottom. AIR, OCEAN, FTL, LTL, EXPRESS.

Requirements
Must have
• We need new business cards. SLEAK SIMPLE FINANCE. They must include a place for NAME, TITLE, CELL, OFFICE PHONE, EMAIL. they also must include our services across the bottom. AIR, OCEAN, FTL, LTL, EXPRESS.
Nice to have
• USE THE COLORS AND LOGO IN THE BRAND GUIDE :)

```html
<!DOCTYPE html>
<html lang="en">
<head>
<meta charset="utf-8">
<title>TORLEX, Inc. Business Cards</title>
<link rel="stylesheet" href="https://fonts.googleapis.com/css2?family=Montserrat:wght@400;500&family=Roboto:wght@400;500&display=swap">
<style>
  :root {
    --backdrop: #b3a78f;
    --card-white: #ebeae6;
    --card-sand: #bdb398;
    --gold: #c1b493;
    --ink: #5f5f5f;
    --rule: #6a6a6a;
    --service-white: #f4f2ec;
  }
  * { margin: 0; padding: 0; box-sizing: border-box; }
  html, body { width: 1200px; height: 900px; overflow: hidden; }
  body { background: var(--backdrop); position: relative; }

  .card {
    position: absolute;
    left: 353px;
    width: 490px;
    height: 317px;
    box-shadow: 0 6px 14px rgba(60, 50, 35, 0.28);
  }
  .card--front { top: 92px; background: var(--card-white); }
  .card--back { top: 456px; background: var(--card-sand); }

  .wordmark {
    position: absolute;
    font-family: "Montserrat", sans-serif;
    font-weight: 500;
    color: var(--gold);
    letter-spacing: 0.08em;
  }
  .card--front .wordmark {
    left: 43px; top: 138px; width: 180px;
    text-align: center; font-size: 32px; line-height: 40px;
  }
  .card--back .wordmark {
    left: 0; right: 0; top: 104px;
    text-align: center; font-size: 64px; line-height: 72px;
    color: #cfc7b0;
  }

  .divider {
    position: absolute;
    left: 240px; top: 77px;
    width: 1.5px; height: 163px;
    background: var(--rule);
  }

  .contact-block {
    position: absolute;
    left: 257px; top: 74px;
    color: var(--ink);
  }
  .contact-block__name {
    font-family: "Roboto", sans-serif;
    font-weight: 500;
    font-size: 16.5px;
    line-height: 20px;
    color: var(--gold);
    letter-spacing: 0.01em;
  }
  .contact-block__title {
    font-family: "Roboto", sans-serif;
    font-size: 14.5px;
    line-height: 18px;
  }
  .contact-block__address {
    margin-top: 12px;
    font-family: "Montserrat", sans-serif;
    font-size: 13.5px;
    line-height: 17px;
  }
  .contact-list {
    list-style: none;
    margin-top: 11px;
    font-family: "Montserrat", sans-serif;
    font-size: 13.5px;
  }
  .contact-list li {
    display: flex;
    align-items: center;
    height: 18.6px;
  }
  .contact-list svg {
    width: 13px; height: 13px;
    margin-right: 7px;
    fill: var(--gold);
    flex: none;
  }

  .services {
    position: absolute;
    left: 0; right: 0; top: 263px;
    text-align: center;
    font-family: "Montserrat", sans-serif;
    font-size: 16px;
    letter-spacing: 0.01em;
    color: var(--service-white);
    word-spacing: 2px;
  }
  .services span + span { margin-left: 8px; }
</style>
</head>
<body>

  <section class="card card--front">
    <div class="wordmark">TORLEX</div>
    <div class="divider"></div>
    <div class="contact-block">
      <p class="contact-block__name">DANIEL WHITCOMBE</p>
      <p class="contact-block__title">Managing Director</p>
      <p class="contact-block__address">2280 Harbor Point Rd Ste 410<br>Lakeview, WA 98104</p>
      <ul class="contact-list">
        <li>
          <svg viewBox="0 0 16 16" aria-hidden="true"><path d="M1 5c0-2 3-3 7-3s7 1 7 3v1.5h-3.5V5h-7v1.5H1z"/><path d="M3 8l2-2h6l2 2v6H3z"/><circle cx="8" cy="10.5" r="1.8" fill="#ebeae6"/></svg>
          555.318.2047
        </li>
        <li>
          <svg viewBox="0 0 16 16" aria-hidden="true"><path d="M4 1h8v14H4z M5.5 2.5v9.5h5V2.5z"/></svg>
          555.642.7791
        </li>
        <li>
          <svg viewBox="0 0 16 16" aria-hidden="true"><path d="M1 4h14v1L8 9.5 1 5z M1 6.5l7 4.5 7-4.5V12H1z"/></svg>
          daniel@torlexinc.com
        </li>
        <li>
          <svg viewBox="0 0 16 16" aria-hidden="true"><circle cx="8" cy="8" r="6.5"/><path d="M5 4c1 1 2 1 2 2.5S5 8 5.5 9.5 8 11 8 13" stroke="#ebeae6" stroke-width="1.2" fill="none"/></svg>
          www.torlexinc.com
        </li>
      </ul>
    </div>
  </section>

  <section class="card card--back">
    <div class="wordmark">TORLEX</div>
    <p class="services">
      <span>• AIR</span><span>• OCEAN</span><span>• FTL</span><span>• LTL</span><span>• EXPRESS.</span>
    </p>
  </section>

</body>
</html>
```